Tane's Fireside CD cover design

I want to design the CD cover for a show. The title of the DVD is Elder Pouli Malaga "Tides of Home". You can see the reference of the old cd cover. At this time, we would like to make it look more classic design.
You can also based on the image 4158 of him to design.
The CD should have the information and stories inside also similar to the scan.

Colors
ec1f27

Requirements
Must have
• Just update the picture of the coconut tree that we have taken for you guys to design. Please crop the 4471 picture close the root of the coconut tree.
Nice to have
• the beach

```html
<!DOCTYPE html>
<html lang="en">
<head>
<meta charset="UTF-8">
<title>Tane's Fireside – Elder Pouli Malaga "Tides of Home" CD Inner Spread</title>
<link href="https://fonts.googleapis.com/css2?family=Architects+Daughter&display=swap" rel="stylesheet">
<style>
  :root {
    --stage: #5a8796;
    --night-deep: #141421;
    --night-mid: #2a2536;
    --night-violet: #3a2f45;
    --fire-glow: #c9692a;
    --fire-hot: #f2b15a;
    --tray: #2b2b2e;
    --tray-edge: #3a3a3e;
    --hub: #7d7d80;
    --hub-inner: #4a4a4d;
    --disc-rim: #d9d9db;
    --ink: #f2eee8;
    --accent: #ec1f27;
  }
  * { margin: 0; padding: 0; box-sizing: border-box; }
  html, body { width: 1200px; height: 692px; overflow: hidden; }
  body {
    background: var(--stage);
    position: relative;
    font-family: "Architects Daughter", cursive;
  }
  .spread {
    position: absolute;
    left: 90px;
    top: 86px;
    width: 1020px;
    height: 520px;
    display: flex;
  }
  .panel {
    position: relative;
    width: 510px;
    height: 520px;
    overflow: hidden;
  }
  .booklet-photo {
    position: absolute;
    inset: 0;
    background:
      radial-gradient(ellipse 60% 40% at 95% 100%, var(--fire-hot) 0%, var(--fire-glow) 25%, rgba(201,105,42,0) 70%),
      linear-gradient(180deg, var(--night-deep) 0%, var(--night-mid) 55%, var(--night-violet) 100%);
  }
  .booklet-text {
    position: absolute;
    left: 0;
    top: 28px;
    width: 100%;
    color: var(--ink);
  }
  .artist {
    text-align: center;
    font-size: 21px;
    letter-spacing: 0.5px;
    margin-left: -40px;
  }
  .album-title {
    text-align: center;
    font-size: 24px;
    font-weight: 400;
    letter-spacing: 1px;
    margin: 6px 0 0 -40px;
  }
  .tracklist {
    list-style: none;
    margin: 30px 0 0 150px;
    font-size: 19px;
    line-height: 26.5px;
  }
  .panel--tray {
    background: linear-gradient(135deg, var(--tray-edge) 0%, var(--tray) 60%);
  }
  .disc {
    position: absolute;
    left: 35px;
    top: 40px;
    width: 440px;
    height: 440px;
  }
</style>
</head>
<body>
  <main class="spread">
    <section class="panel panel--booklet">
      <div class="booklet-photo" role="img" aria-label="Night sky full of stars with silhouetted coconut palms and campfire sparks glowing at the lower right"></div>
      <div class="booklet-text">
        <p class="artist">Elder Pouli Malaga</p>
        <h1 class="album-title">"TIDES OF HOME"</h1>
        <ol class="tracklist">
          <li>01. Salt on the Breeze</li>
          <li>02. Lanterns Ashore</li>
          <li>03. Tides of Home</li>
          <li>04. Slow Canoe Homeward</li>
          <li>05. Stars over the Reef</li>
          <li>06. Ember Dance</li>
          <li>07. Where the Palms Lean</li>
          <li>08. Driftwood Lullaby</li>
          <li>09. Last Light on Sand</li>
        </ol>
      </div>
    </section>

    <section class="panel panel--tray">
      <svg class="disc" viewBox="0 0 440 440">
        <defs>
          <radialGradient id="disc-art" cx="0.72" cy="0.45" r="0.7">
            <stop offset="0" stop-color="#c43a1a"/>
            <stop offset="0.35" stop-color="#5a2a2a"/>
            <stop offset="0.7" stop-color="#1c1f33"/>
            <stop offset="1" stop-color="#141628"/>
          </radialGradient>
        </defs>
        <circle cx="220" cy="220" r="218" fill="var(--disc-rim)"/>
        <circle cx="220" cy="220" r="213" fill="url(#disc-art)" role="img" aria-label="Firelit portrait of the performer against a starry sky with palm silhouettes"/>
        <circle cx="220" cy="220" r="78" fill="var(--hub)"/>
        <circle cx="220" cy="220" r="36" fill="var(--hub-inner)"/>
        <circle cx="220" cy="220" r="16" fill="var(--tray)"/>
      </svg>
    </section>
  </main>
</body>
</html>
```